Tamarack Hearth Partners Business Card

Looking for a new business card layout. We are a real estate firm w/ a logo, old design attached. Must keep the same elements on there, just need a fresh look and possible some foil accents. Looking for a simpler design w/ more modern style.

Target Market(s)

Real Estate clients

Industry/Entity Type

Real Estate Agent

Contact Information for Business Card

see attached

Font styles to use
Sans Serif

Requirements
Must have
• all elements on current biz card
Nice to have
• modern look, simpler than we have!
Should not have
• no serif fonts

```html
<!DOCTYPE html>
<html lang="en">
<head>
<meta charset="utf-8">
<title>Tamarack Hearth Partners – Business Card</title>
<link rel="stylesheet" href="https://fonts.googleapis.com/css2?family=Lato:wght@300;400;700;900&display=swap">
<style>
  :root {
    --page-bg: #e6e7e9;
    --brand-blue: #00adee;
    --stripe-blue: #1a7fc8;
    --white: #ffffff;
    --soft-white: #e9eef1;
    --photo-light: #e9e2d6;
    --photo-mid: #cdb48c;
    --photo-teal: #3cc6bd;
  }
  * { margin: 0; padding: 0; box-sizing: border-box; }
  html, body { width: 1200px; height: 1200px; overflow: hidden; }
  body {
    background: var(--page-bg);
    font-family: "Lato", Arial, sans-serif;
    color: var(--white);
    position: relative;
  }
  .card {
    position: absolute;
    left: 194px;
    width: 809px;
    height: 462px;
    background: var(--brand-blue);
    overflow: hidden;
  }
  .card--front { top: 106px; }
  .card--back { top: 628px; }

  .portrait {
    position: absolute;
    left: 0; top: 0;
    width: 346px; height: 462px;
    background:
      radial-gradient(ellipse 45% 38% at 50% 40%, #e3b99a 0%, rgba(227,185,154,0) 100%),
      linear-gradient(180deg, var(--photo-light) 0%, var(--photo-mid) 45%, var(--photo-teal) 80%, var(--photo-teal) 100%);
  }
  .portrait-edge {
    position: absolute;
    left: 346px; top: 0;
    width: 10px; height: 462px;
    background: var(--stripe-blue);
  }

  .brand-name {
    position: absolute;
    color: var(--white);
    text-transform: uppercase;
    line-height: 1;
  }
  .brand-name span { display: block; white-space: nowrap; }
  .brand-name .brand-line-1 { font-size: 37px; font-weight: 900; letter-spacing: -0.5px; }
  .brand-name .brand-line-2 {
    font-size: 27px;
    font-weight: 400;
    color: var(--soft-white);
    letter-spacing: 22px;
    margin-top: 6px;
  }
  .card--front .brand-name { left: 393px; top: 184px; }
  .card--back .brand-name { left: 39px; top: 60px; }

  .divider {
    position: absolute;
    left: 0; top: 162px;
    width: 577px; height: 6px;
    background: var(--white);
  }

  .agent {
    position: absolute;
    right: 37px; top: 131px;
    text-align: right;
  }
  .agent-name { font-size: 36px; font-weight: 900; letter-spacing: -0.5px; line-height: 1; white-space: nowrap; }
  .agent-title { font-size: 21px; font-weight: 400; line-height: 1; margin-top: 4px; white-space: nowrap; }

  .contact-list {
    position: absolute;
    left: 39px; top: 192px;
    list-style: none;
  }
  .contact-item {
    display: flex;
    align-items: center;
    height: 34px;
    font-size: 21px;
    font-weight: 700;
    white-space: nowrap;
  }
  .contact-item:first-child { height: 36px; }
  .contact-item--tall { height: 58px; margin-top: 2px; }
  .contact-item--tall .contact-text { line-height: 1.3; }
  .contact-icon {
    width: 28px; height: 28px;
    margin-right: 15px;
    flex: none;
    fill: var(--white);
  }
</style>
</head>
<body>

<section class="card card--front">
  <div class="portrait" role="img" aria-label="Portrait photo of the broker"></div>
  <div class="portrait-edge"></div>
  <div class="brand-name">
    <span class="brand-line-1">Tamarack Hearth</span>
    <span class="brand-line-2">Partners</span>
  </div>
</section>

<section class="card card--back">
  <div class="brand-name">
    <span class="brand-line-1">Tamarack Hearth</span>
    <span class="brand-line-2">Partners</span>
  </div>
  <div class="divider"></div>

  <div class="agent">
    <div class="agent-name">Nora Vance</div>
    <div class="agent-title">Principle Broker</div>
  </div>

  <ul class="contact-list">
    <li class="contact-item">
      <svg class="contact-icon" viewBox="0 0 28 28" aria-hidden="true">
        <path d="M2 9c0-4 5-6 12-6s12 2 12 6v2h-6V8c-2-1-10-1-12 0v3H2z"/>
        <path d="M7 12h14l3 13H4z"/>
        <rect x="10" y="16" width="8" height="6" fill="#00adee"/>
      </svg>
      <span class="contact-text">555.014.7222</span>
    </li>
    <li class="contact-item">
      <svg class="contact-icon" viewBox="0 0 28 28" aria-hidden="true">
        <path d="M6 3l4 5-2 3c1 3 4 6 7 7l3-2 5 4-3 4C12 24 4 16 3 7z"/>
        <path d="M16 4a9 9 0 0 1 8 8h-2a7 7 0 0 0-6-6z"/>
        <path d="M16 8a5 5 0 0 1 4 4h-2a3 3 0 0 0-2-2z"/>
      </svg>
      <span class="contact-text">555.019.4208</span>
    </li>
    <li class="contact-item">
      <svg class="contact-icon" viewBox="0 0 28 28" aria-hidden="true">
        <path d="M2 6h24v16H2z"/>
        <path d="M2 6l12 10L26 6M2 22l9-8M26 22l-9-8" fill="none" stroke="#00adee" stroke-width="1.8"/>
      </svg>
      <span class="contact-text">nora@tamarackhearth.com</span>
    </li>
    <li class="contact-item">
      <svg class="contact-icon" viewBox="0 0 28 28" aria-hidden="true">
        <circle cx="14" cy="14" r="12"/>
        <g fill="none" stroke="#00adee" stroke-width="1.4">
          <ellipse cx="14" cy="14" rx="5" ry="12"/>
          <path d="M14 2v24M2 14h24M4 8h20M4 20h20"/>
        </g>
      </svg>
      <span class="contact-text">www.TamarackHearth-Homes.com</span>
    </li>
    <li class="contact-item contact-item--tall">
      <svg class="contact-icon" viewBox="0 0 28 28" aria-hidden="true">
        <path d="M14 1a9 9 0 0 1 9 9c0 7-9 17-9 17S5 17 5 10a9 9 0 0 1 9-9z"/>
        <circle cx="14" cy="10" r="3.3" fill="#00adee"/>
      </svg>
      <span class="contact-text">218 NW Juniper Ln Ridgefield,<br>OR 97999</span>
    </li>
  </ul>
</section>

</body>
</html>
```